Aviation Banner Ad Designs

SkyLedgerMetrics provides access to the most accurate aircraft operating cost information, to compare Piston, Turboprop and Jet aircraft.

The banners ads will be used for retargeting/remarketing - to bring visitors back to the site. The banners should remind and reinforce the key messages of what the site provides.

Target Market(s)

Private aircraft buyers including:
- Aircraft Brokers
- Charter Operators
- Corporate Flight Departments
- Aircraft Management companies
- Financial Institutions
- Aircraft Owners
- Prospective Buyers

Requirements
Must have
• A. Banner Objective
The visual and textual content of the banner should remind the viewer about the features of the site, and prompt them to return to the site.
1. Arresting visual
2. Headline
3. Single message
4. Compelling CTA
5. Logo - big enough to see
6. Standard DWR ad sizes/specs

B. Design Elements
Logo: As attached
Main Title: Calculate Jet Operating Costs
Subtitle: Compare Ownership Usage Scenarios
Call to Action Button: Compare Ownership Costs
Background: Several images supplied as options

C. Banner Sizes
Do examples as 300×250 , 728×90 , 160×600
Final sizes to also include 320×100 , 336x280 , 300x600

Finally delivery as .jpg files.

Font - use same font as on site

```html
<!DOCTYPE html>
<html lang="en">
<head>
<meta charset="utf-8">
<title>SkyLedgerMetrics – Calculate Jet Operating Costs</title>
<link rel="stylesheet" href="https://fonts.googleapis.com/css2?family=Teko:wght@500&family=Fira+Sans+Condensed:wght@400;500&display=swap">
<style>
  :root {
    --page-bg: #e6eaef;
    --paper: #f2f1ee;
    --paper-shade: #e4e3df;
    --brand-red: #d5232b;
    --brand-red-dark: #b0161d;
    --brand-blue: #1c63a3;
    --brand-blue-deep: #114f8a;
    --flag-green: #2a9a3a;
    --ink: #262626;
    --white: #ffffff;
    --bullet-green: #3fbf4a;
  }
  html, body {
    margin: 0;
    width: 1200px;
    height: 900px;
    overflow: hidden;
    background: var(--page-bg);
  }
  .banner {
    position: absolute;
    left: 20px;
    top: 239px;
    width: 1160px;
    height: 422px;
    box-shadow: 0 6px 18px rgba(0,0,0,.18);
  }
  .headline {
    font-family: "Teko", "Arial Narrow", sans-serif;
    font-weight: 500;
    fill: var(--white);
  }
  .subtitle {
    font-family: "Teko", "Arial Narrow", sans-serif;
    font-weight: 500;
    fill: var(--ink);
  }
  .cta-label {
    font-family: "Teko", "Arial Narrow", sans-serif;
    font-weight: 500;
    fill: var(--white);
  }
  .brand-name {
    font-family: "Fira Sans Condensed", "Arial Narrow", sans-serif;
    font-weight: 500;
    fill: var(--ink);
  }
  .audience-item {
    font-family: "Fira Sans Condensed", "Arial Narrow", sans-serif;
    font-weight: 400;
    font-size: 26px;
    fill: var(--white);
  }
  .audience-bullet {
    fill: var(--brand-blue-deep);
    stroke: var(--bullet-green);
    stroke-width: 3.5;
  }
</style>
</head>
<body>
<svg class="banner" viewBox="0 0 1160 422" xmlns="http://www.w3.org/2000/svg">
  <defs>
    <linearGradient id="paperFill" x1="0" y1="0" x2="1" y2="1">
      <stop offset="0" stop-color="var(--paper)"/>
      <stop offset="1" stop-color="var(--paper-shade)"/>
    </linearGradient>
    <linearGradient id="bandFadeTop" x1="0" y1="0" x2="1" y2="0">
      <stop offset="0" stop-color="var(--brand-red)"/>
      <stop offset="0.6" stop-color="var(--brand-red)"/>
      <stop offset="1" stop-color="var(--brand-red)" stop-opacity="0"/>
    </linearGradient>
    <linearGradient id="bandFadeLower" x1="0" y1="0" x2="1" y2="0">
      <stop offset="0" stop-color="var(--brand-red)"/>
      <stop offset="0.72" stop-color="var(--brand-red)"/>
      <stop offset="1" stop-color="var(--brand-red)" stop-opacity="0.15"/>
    </linearGradient>
    <linearGradient id="blueFill" x1="0" y1="0" x2="1" y2="1">
      <stop offset="0" stop-color="var(--brand-blue)"/>
      <stop offset="1" stop-color="var(--brand-blue-deep)"/>
    </linearGradient>
    <linearGradient id="skyPhoto" x1="0" y1="0" x2="0" y2="1">
      <stop offset="0" stop-color="#5f86c2"/>
      <stop offset="0.55" stop-color="#c9d3de"/>
      <stop offset="1" stop-color="#8aa6c8"/>
    </linearGradient>
    <linearGradient id="cabinPhoto" x1="0" y1="0" x2="1" y2="1">
      <stop offset="0" stop-color="#8fa3c2"/>
      <stop offset="0.5" stop-color="#d9c9a0"/>
      <stop offset="1" stop-color="#a8935f"/>
    </linearGradient>
    <linearGradient id="devicePhoto" x1="0" y1="0" x2="0" y2="1">
      <stop offset="0" stop-color="#f3f4f6"/>
      <stop offset="1" stop-color="#c9ced6"/>
    </linearGradient>
  </defs>

  <!-- light panel -->
  <rect class="paper" x="0" y="0" width="1160" height="422" fill="url(#paperFill)"/>

  <!-- headline bands -->
  <rect class="headline-band" x="0" y="43" width="720" height="105" fill="url(#bandFadeTop)"/>
  <rect class="headline-band" x="0" y="159" width="640" height="104" fill="url(#bandFadeLower)"/>

  <text class="headline" x="37" y="139" font-size="112" textLength="405" lengthAdjust="spacingAndGlyphs">CALCULATE JET</text>
  <text class="headline" x="37" y="251" font-size="112" textLength="491" lengthAdjust="spacingAndGlyphs">OPERATING COSTS</text>

  <text class="subtitle" x="37" y="309" font-size="46" textLength="492" lengthAdjust="spacingAndGlyphs">COMPARE OWNERSHIP USAGE SCENARIOS</text>

  <!-- call to action -->
  <g class="cta-button">
    <rect x="37" y="340" width="290" height="40" rx="20" fill="var(--brand-red)" stroke="var(--brand-red-dark)" stroke-width="2"/>
    <text class="cta-label" x="56" y="372" font-size="32" textLength="252" lengthAdjust="spacingAndGlyphs">COMPARE OWNERSHIP COSTS</text>
  </g>

  <!-- brand name -->
  <g class="brand">
    <rect x="345" y="348" width="14" height="14" fill="var(--brand-red)"/>
    <text class="brand-name" x="368" y="363" font-size="24">SkyLedgerMetrics</text>
  </g>

  <!-- blue audience panel with flag stripe -->
  <polygon class="flag-stripe-green" points="726,0 740,0 610,422 596,422" fill="var(--flag-green)"/>
  <polygon class="flag-stripe-white" points="730,0 736,0 606,422 600,422" fill="var(--white)"/>
  <polygon class="flag-stripe-red" points="736,0 746,0 616,422 606,422" fill="var(--brand-red)"/>
  <polygon class="audience-panel" points="744,0 1160,0 1160,422 614,422" fill="url(#blueFill)"/>

  <!-- photo circles -->
  <circle cx="688" cy="134" r="77" fill="url(#skyPhoto)" stroke="var(--white)" stroke-width="3" role="img" aria-label="Close-up photo of a business jet engine and tail against the sky"/>
  <circle cx="632" cy="301" r="78" fill="url(#cabinPhoto)" stroke="var(--white)" stroke-width="3" role="img" aria-label="Photo of a business jet with its boarding stairs open"/>

  <!-- device mockup area -->
  <rect x="1002" y="248" width="146" height="124" rx="6" fill="url(#devicePhoto)" opacity="0.9" role="img" aria-label="Illustration of phone, tablet, desktop and laptop screens showing cost charts"/>

  <!-- audience list -->
  <g class="audience-list">
    <circle class="audience-bullet" cx="788" cy="96" r="5.5"/>
    <text class="audience-item" x="806" y="104" textLength="321" lengthAdjust="spacingAndGlyphs">Aircraft Management companies</text>
    <circle class="audience-bullet" cx="788" cy="139" r="5.5"/>
    <text class="audience-item" x="806" y="147" textLength="294" lengthAdjust="spacingAndGlyphs">Corporate Flight Departments</text>
    <circle class="audience-bullet" cx="788" cy="183" r="5.5"/>
    <text class="audience-item" x="806" y="191" textLength="208" lengthAdjust="spacingAndGlyphs">Financial Institutions</text>
    <circle class="audience-bullet" cx="788" cy="226" r="5.5"/>
    <text class="audience-item" x="806" y="234" textLength="190" lengthAdjust="spacingAndGlyphs">Prospective Buyers</text>
    <circle class="audience-bullet" cx="788" cy="269" r="5.5"/>
    <text class="audience-item" x="806" y="277" textLength="180" lengthAdjust="spacingAndGlyphs">Charter Operators</text>
    <circle class="audience-bullet" cx="788" cy="313" r="5.5"/>
    <text class="audience-item" x="806" y="321" textLength="158" lengthAdjust="spacingAndGlyphs">Aircraft Brokers</text>
    <circle class="audience-bullet" cx="788" cy="356" r="5.5"/>
    <text class="audience-item" x="806" y="364" textLength="158" lengthAdjust="spacingAndGlyphs">Aircraft Owners</text>
  </g>
</svg>
</body>
</html>
```